Post Disaster Temporary Housing Literature Review poster

Wanting a poster design for two Emergency Management conferences we have coming up. The information to be included in the poster is capturing the purpose, findings and recommendations from a post disaster temporary housing literature review looking at “What should government consider in order to improve planning and decision making for accommodation needs after a disaster, and to support people’s transition to stable housing?”
I’d like to enhance the visual appeal through including relevant images or graphic. I am also open to reducing the text if needed.
The government group I work with focuses on the social and human side of disaster recovery so keen for any images to reflect the human aspect and not focus solely on disasters or housing.
Government and NGO's

```html
<!DOCTYPE html>
<html lang="en">
<head>
<meta charset="utf-8">
<title>Post Disaster Temporary Housing Literature Review</title>
<link href="https://fonts.googleapis.com/css2?family=Poppins:wght@300;400;500;600;700;800&display=swap" rel="stylesheet">
<style>
:root{
  --navy:#0e2433;
  --navy-2:#14364c;
  --accent:#1b84b6;
  --accent-bright:#2aa0d8;
  --title-blue:#137fae;
  --pill-grey:#c9ced3;
  --text-dark:#1b1f23;
  --white:#ffffff;
  --stage:#ececec;
}
*{margin:0;padding:0;box-sizing:border-box}
html,body{width:822px;height:1200px;overflow:hidden;background:var(--stage)}
body{font-family:"Poppins",sans-serif;color:var(--text-dark)}
.poster{position:absolute;left:161px;top:0;width:500px;height:1200px;background:var(--white);overflow:hidden}
.abs{position:absolute}

/* header */
.header{left:0;top:0;width:500px;height:166px;background:var(--navy)}
.header-photo{right:0;top:0;width:200px;height:166px;background:linear-gradient(90deg,var(--navy) 0%,#3b3430 35%,#6b4a34 65%,#4a3a30 100%)}
.title-post{left:34px;top:30px;font-size:63px;font-weight:800;color:var(--white);letter-spacing:-1.5px;line-height:1}
.title-disaster{left:34px;top:84px;font-size:38px;font-weight:800;color:var(--white);letter-spacing:-1.5px;line-height:1}
.title-side{left:226px;top:32px;font-size:21.5px;line-height:22px;color:var(--white);font-weight:300;letter-spacing:.3px}
.title-side .lead{font-weight:800;color:var(--accent-bright)}
.report-line{left:34px;top:132px;color:var(--white);display:flex;align-items:center;gap:6px}
.report-line .kind{font-size:6.2px;letter-spacing:1px;font-weight:400}
.report-line .sep{width:1px;height:10px;background:var(--accent-bright)}
.report-line .date{font-size:12.5px;font-weight:700}
.report-line .date span{font-weight:300;color:var(--accent-bright)}

.url-bar{left:32px;top:157px;width:436px;height:19px;border-radius:10px;background:var(--pill-grey);display:flex;align-items:center;white-space:nowrap;overflow:hidden}
.url-bar .label{font-size:6.6px;font-weight:500;padding-left:12px;width:138px;flex:none;color:var(--navy)}
.url-bar .link{flex:1;height:19px;border-radius:10px;background:var(--accent);color:var(--white);font-size:7.4px;font-weight:500;display:flex;align-items:center;padding-left:8px;white-space:nowrap;overflow:hidden}

.tab{height:20px;background:var(--navy);color:var(--white);font-weight:700;font-size:11.5px;display:flex;align-items:center;justify-content:center;clip-path:polygon(0 0,100% 0,92% 100%,8% 100%)}
.tab-purpose{left:195px;top:176px;width:110px}

.purpose-text{left:34px;top:209px;width:432px;text-align:center;font-size:6.5px;line-height:8px}
.question{left:30px;top:247px;width:440px;text-align:center;font-size:8.8px;line-height:11px;font-weight:700;color:var(--navy)}
.commission{left:44px;top:276px;width:412px;text-align:center;font-size:6.5px;line-height:8px}

/* findings */
.findings-photo{left:0;top:300px;width:500px;height:160px;background:linear-gradient(180deg,rgba(255,255,255,1) 0%,#dcdfe2 30%,#8b8a86 65%,#4d4640 100%)}
.findings-title{left:0;top:318px;width:500px;text-align:center;font-size:15px;font-weight:700;color:var(--navy)}
.dark-zone{left:0;top:457px;width:500px;height:560px;background:linear-gradient(180deg,#1d4862 0%,#143a52 35%,#0f2c40 70%,#163c55 100%)}
.card{top:345px;width:138px;height:260px;background:var(--white);border:2px solid var(--navy);border-radius:10px;padding:10px 9px 0 11px}
.card h3{font-size:9.4px;line-height:11.4px;font-weight:600;color:var(--title-blue);width:90px}
.card .icon{position:absolute;right:8px;top:16px;width:28px;height:26px}
.card p{font-size:5.7px;line-height:7.1px;margin-top:6px}
.card ul{list-style:none;margin-top:4px}
.card li{font-size:4.6px;line-height:5.7px;padding-left:6px;position:relative;margin-bottom:4px}
.card li::before{content:"";position:absolute;left:0;top:1px;width:4px;height:4px;border-radius:50%;background:#2eb872}
.card-1{left:39px}
.card-2{left:182px}
.card-3{left:324px}

/* recommendations */
.rec-title{left:0;top:628px;width:500px;text-align:center;font-size:15px;font-weight:700;color:var(--white)}
.rec{width:200px;color:var(--white)}
.rec .tag{display:inline-block;background:var(--accent);color:var(--white);font-weight:600;font-size:9px;line-height:13px;padding:0 7px;border-radius:5px}
.rec p{font-size:7px;line-height:8.4px;margin-top:4px;font-weight:400}
.rec-left{left:40px}
.rec-right{left:262px;width:205px}
.research-list{display:grid;grid-template-columns:1fr 1fr;gap:5px 8px;margin-top:5px;list-style:none}
.research-list li{font-size:5px;line-height:5.9px;padding-left:7px;position:relative}
.research-list li::before{content:"";position:absolute;left:0;top:1px;width:4px;height:4px;border-radius:50%;background:#2eb872}

.rule{left:0;top:1017px;width:500px;height:2px;background:var(--accent)}
.tab-next{left:186px;top:1018px;width:128px;background:var(--accent)}

.next-text{left:38px;top:1057px;width:190px;font-size:6.6px;line-height:8.1px}
.people{left:242px;top:1052px;width:226px;height:66px;display:flex}
.person{flex:1;text-align:center;position:relative}
.person + .person::before{content:"";position:absolute;left:0;top:2px;width:1px;height:52px;background:#d7dbdf}
.person .disc{width:37px;height:37px;border-radius:50%;margin:0 auto;border:2.5px solid #bfe3f3;display:flex;align-items:center;justify-content:center}
.person .disc span{width:28px;height:28px;border-radius:50%;display:block}
.person .name{font-size:7px;line-height:8.5px;font-weight:600;margin-top:5px;color:var(--navy)}

.org-mark{left:36px;top:1138px;display:flex;align-items:center;gap:7px}
.org-mark .dot{width:32px;height:32px;border-radius:50%;border:2px solid var(--accent)}
.org-mark .name{font-size:8.6px;line-height:10.5px;font-weight:400;color:var(--navy)}
.contact{right:36px;top:1138px;text-align:right;color:var(--navy)}
.contact .lead{font-size:7px}
.contact .mail{font-size:8.4px;font-weight:500;display:flex;align-items:center;justify-content:flex-end;gap:3px}
.contact .web{font-size:12px;font-weight:600;letter-spacing:1.2px;margin-top:2px}
.contact .web span{color:var(--accent)}
</style>
</head>
<body>
<main class="poster">

  <header class="abs header"></header>
  <div class="abs header-photo" role="img" aria-label="Photograph of a fire-damaged brick house interior"></div>
  <h1 class="abs title-post">POST</h1>
  <div class="abs title-disaster">DISASTER</div>
  <div class="abs title-side"><span class="lead">TEMPORARY</span><br>HOUSING<br>LITERATURE<br>REVIEW</div>
  <div class="abs report-line"><span class="kind">SUMMARY REPORT</span><span class="sep"></span><span class="date">JANUARY <span>2024</span></span></div>

  <div class="abs url-bar"><span class="label">THE FULL REPORT IS AVAILABLE AT</span><span class="link">https://knowledge.recoveryhub.org.au/resources/recovery-group</span></div>
  <div class="abs tab tab-purpose">PURPOSE</div>

  <p class="abs purpose-text">There are currently significant challenges in supporting displaced people with timely and equitable access to emergency and temporary accommodation and assisting them on a path to stable housing in the aftermath of a disaster. This report seeks to support agencies and decision makers to formulate and implement appropriate approaches to post-disaster housing, factoring in the scale of a disaster and varying community cohorts. The central research question underpinning this report is:</p>
  <p class="abs question">What should government consider in order to improve planning and decision making for accommodation needs after a disaster, and to support people’s transition to stable housing?</p>
  <p class="abs commission">The full report was commissioned by the Community Recovery Advisory Group (CRAG) and undertaken by Helen Marsh and David Ortis through the Eastbank Institute of Technology (EIT). The findings and recommendations may be utilised by stakeholders.</p>

  <div class="abs findings-photo" role="img" aria-label="Photograph of a collapsed, burnt timber roof frame"></div>
  <div class="abs dark-zone" role="img" aria-label="Dark blue toned photograph of a damaged weatherboard house"></div>
  <h2 class="abs findings-title">FIINDINGS</h2>

  <article class="abs card card-1">
    <h3>Leading practice in disaster housing recovery</h3>
    <svg class="icon" viewBox="0 0 28 26" aria-hidden="true"><path d="M3 14 Q8 6 14 10 Q10 11 10 14 Z" fill="#0e2433"/><path d="M16 12 L22 6 L27 11 V16 H17 Z" fill="#0e2433"/><path d="M1 18 Q5 15 9 18 T17 18 T27 18 V21 Q23 18 19 21 T11 21 T1 21 Z" fill="#0e2433"/><path d="M1 23 Q5 20 9 23 T17 23 T27 23 V26 H1 Z" fill="#0e2433"/></svg>
    <p>The analysis of leading practices in housing recovery led to the development of a checklist of actions that could be used to identify appropriate actions by housing recovery officers and their agencies in providing and managing emergency and short-term accommodation and temporary housing. The checklist was developed from research and contains criteria for achieving eight categories of leading practice: Community Engagement &amp; Participation, Location, Safety, Health, Comfort &amp; Privacy, Cultural &amp; Special Needs, Community &amp; Connection, and Social &amp; Technical Support Services.</p>
  </article>

  <article class="abs card card-2">
    <h3>Innovative approaches to temporary housing</h3>
    <svg class="icon" viewBox="0 0 28 26" aria-hidden="true"><path d="M14 2 L27 13 L25 15 L14 6 L3 15 L1 13 Z" fill="#0e2433"/><path d="M5 14 L14 7 L23 14 V25 H17 V18 H11 V25 H5 Z" fill="#0e2433"/><rect x="20" y="3" width="3" height="6" fill="#0e2433"/></svg>
    <p>Innovative approaches to effective temporary housing practices are based upon the concept of resilient housing recovery, which has at least five dimensions: Wellbeing, Liveability, Sustainability, Community Connection, and Viability. This change of focus has two major implications:</p>
    <ul>
      <li>The planning of post-disaster housing and infrastructure programs needs to be become one of the priority strategies in pre-disaster preparation; and</li>
      <li>Strategies are needed to establish Temporary Housing as the first step in the design and construction of on-site Stable Housing to minimise the social, economic and environmental costs incurred when displaced people spend extended periods of time in Temporary Housing.</li>
    </ul>
    <p style="margin-top:0">These implications are explored through strategies and tools for pre-disaster planning and the development of a two-phase model for constructing Stable Housing through a “temporary-to-permanent” construction strategy.</p>
  </article>

  <article class="abs card card-3">
    <h3>A decision making framework for resilient housing recovery</h3>
    <svg class="icon" viewBox="0 0 28 26" aria-hidden="true"><circle cx="13" cy="7" r="6" fill="#0e2433"/><circle cx="24" cy="4" r="2.5" fill="#0e2433"/><path d="M3 26 V14 L9 10 V26 Z" fill="#0e2433"/><path d="M11 18 L19 11 L27 18 V26 H11 Z" fill="#0e2433"/><rect x="17" y="21" width="4" height="5" fill="#fff"/></svg>
    <p>The Framework seeks to integrate the steps in project management and to use the housing process as a lever for overall recovery. This involves aligning decisions at strategic and operational levels and managing the trade-offs between issues of location, tenure, housing types and procurement.</p>
    <p>There are nine such decision categories in the Framework: Consultation, Pre-Disaster Planning for Housing Recovery, Situation Analysis after a Disaster Event, Recognising Cohorts of Displaced People with Different Needs and Assets, Identifying and Selecting Housing Model Options; Providing AgencyWrap-Around Support Services; Using Housing Decisions to Promote Local Economic and Social Recovery, Program Design and Delivery, and Monitoring and Evaluation.</p>
  </article>

  <h2 class="abs rec-title">RECOMMENDATIONS</h2>

  <section class="abs rec rec-left" style="top:662px">
    <span class="tag">Terminology</span>
    <p>Develop a standard set of terminology to describe the phases and types of accommodation displaced people may access on the path to stable housing and to be adopted by State and Territory recovery agencies. The terms recommended for consideration are: Emergency and Short-Term Accommodation, Temporary Housing and Stable Housing.</p>
  </section>
  <section class="abs rec rec-left" style="top:758px">
    <span class="tag">Principles</span>
    <p>Adopt common principles of leading practice in post-disaster housing recovery including community connection, wellbeing, liveability, viability, and sustainability, for deciding accommodation and support options for people.</p>
  </section>
  <section class="abs rec rec-left" style="top:836px">
    <span class="tag">National Principles</span>
    <p>The Commonwealth and State/Territory governments should extend the agreed principles of disaster recovery to include principles of resilient recovery.</p>
  </section>
  <section class="abs rec rec-left" style="top:899px">
    <span class="tag">Guidelines</span>
    <p>Develop resources and guidelines to support planning and operational response for post disaster temporary housing.</p>
  </section>
  <section class="abs rec rec-left" style="top:957px">
    <span class="tag">Capacity Building</span>
    <p>Develop capacity building resources and programs for State/Territory agencies and local governments to support pre planning for disaster temporary housing.</p>
  </section>

  <section class="abs rec rec-right" style="top:662px">
    <span class="tag">Funding</span>
    <p>Recognise different cost implications of temporary housing programs including indirect costs. Develop funding streams to address the priority needs.</p>
  </section>
  <section class="abs rec rec-right" style="top:723px">
    <span class="tag">Further Research</span>
    <p>Undertake research into post disaster temporary housing topics such as:</p>
    <ul class="research-list">
      <li>Improving housing resilience through land-use planning and building codes.</li>
      <li>Utilisation of innovative construction technologies, materials and methods.</li>
      <li>Learnings from previous disasters on suitable approaches for different communities and contexts.</li>
      <li>Utilising permanent prefabricated housing modules that transition from temporary to permanent.</li>
    </ul>
  </section>
  <section class="abs rec rec-right" style="top:832px">
    <span class="tag">Pilot Project</span>
    <p>Resource, trial and evaluate a pilot program to identify ways of achieving a two-phase approach to assisting home-owners and renter households into stable housing.</p>
  </section>
  <section class="abs rec rec-right" style="top:892px">
    <span class="tag">Decision Making Framework</span>
    <p>Adopt the outline of a Decision-Making Framework for Disaster Housing Recovery provided in this report to provide a basis for the development of tools that can be used by multiple stakeholders in housing recovery programs and projects across different parts of Australia.</p>
  </section>
  <section class="abs rec rec-right" style="top:967px">
    <span class="tag">Capturing Learnings</span>
    <p>Establish a national repository of evaluation reports and support processes for regular cross-case analysis.</p>
  </section>

  <div class="abs rule"></div>
  <div class="abs tab tab-next">NEXT STEPS</div>

  <p class="abs next-text">The Community Recovery Advisory Group is partnering with Hazards Resilience Research Network to analyse previous post-disaster temporary housing assistance and support mechanisms used in Australia. The project aims to provide national guidance on the design and implementation of temporary housing from the research and resources developed.</p>

  <div class="abs people">
    <div class="person"><div class="disc"><span style="background:var(--navy-2)"></span></div><div class="name">Morgan<br>Ellery</div></div>
    <div class="person"><div class="disc"><span style="background:var(--accent)"></span></div><div class="name">National Consultant<br>Disaster Recovery</div></div>
    <div class="person"><div class="disc"><span style="background:var(--accent-bright)"></span></div><div class="name">Community Recovery<br>Advisory Group</div></div>
  </div>

  <div class="abs org-mark">
    <span class="dot"></span>
    <span class="name">Community Recovery<br>Advisory Group<br>AUSTRALIA</span>
  </div>

  <div class="abs contact">
    <div class="lead">For further information contact</div>
    <div class="mail"><svg width="8" height="6" viewBox="0 0 8 6" aria-hidden="true"><rect width="8" height="6" fill="#0e2433"/><path d="M0 0 L4 3.5 L8 0" stroke="#fff" stroke-width=".8" fill="none"/></svg>m.ellery@recoveryplanning.example.gov.au</div>
    <div class="web">www.<span>knowledge</span>.recoveryhub.org.au</div>
  </div>

</main>
</body>
</html>
```